Business cards for a naturopathic day clinic for stem cell therapy

We need a basic design for a day clinic, that offers stem cell therapies for Lyme therapy and other severe chronic illnesses.
Our name is "Haus solvaKrĂ¤ut", which can be translated into "Manor solvaHerb". We are a couple of naturopaths working along side physiotherapists and osteopaths, yoga teachers and massage therapists. I attached our logo.

```html
<!DOCTYPE html>
<html lang="de">
<head>
<meta charset="utf-8">
<title>Haus solvaKräut – Visitenkarten</title>
<link rel="stylesheet" href="https://fonts.googleapis.com/css2?family=Raleway:wght@400;600;700&family=Lato:wght@400&display=swap">
<style>
  :root {
    --backdrop: #a3a3a3;
    --leaf: #b9c962;
    --leaf-soft: #c4d27d;
    --taupe: #8d7d70;
    --ink: #2a2a2a;
    --rule: #8a8a8a;
    --paper: #ffffff;
  }
  * { margin: 0; padding: 0; box-sizing: border-box; }
  html, body { width: 1200px; height: 1200px; overflow: hidden; }
  body {
    background: var(--backdrop);
    position: relative;
    font-family: "Lato", sans-serif;
  }
  .card {
    position: absolute;
    top: 303px;
    width: 370px;
    height: 593px;
    box-shadow: 3px 4px 5px rgba(0,0,0,0.45);
  }
  .card--front { left: 200px; background: var(--leaf); }
  .card--back { left: 599px; width: 365px; background: var(--paper); }

  .brand {
    position: absolute;
    display: flex;
    align-items: center;
    gap: 12px;
    font-family: "Raleway", sans-serif;
    font-weight: 400;
    white-space: nowrap;
  }
  .brand__dot { border-radius: 50%; flex: none; }
  .card--front .brand { left: 40px; top: 488px; color: var(--paper); font-size: 33px; }
  .card--front .brand__dot { width: 22px; height: 22px; background: var(--paper); }
  .card--back .brand { left: 36px; top: 168px; color: var(--leaf); font-size: 33px; }
  .card--back .brand__dot { width: 22px; height: 22px; background: var(--leaf); }

  .person {
    position: absolute;
    top: 336px;
    left: 0; right: 0;
    text-align: center;
  }
  .person__name {
    font-family: "Raleway", sans-serif;
    font-weight: 700;
    font-size: 26px;
    line-height: 30px;
    color: var(--taupe);
  }
  .person__name .surname { color: var(--leaf); }
  .person__role { font-size: 17px; line-height: 20px; color: var(--ink); }

  .icon-row {
    position: absolute;
    top: 396px;
    left: 87px;
    width: 190px;
    display: flex;
    align-items: center;
    gap: 5px;
  }
  .icon-row__rule { flex: 1; height: 1px; background: var(--rule); }
  .icon-row__rule:first-child { margin-right: 3px; }
  .icon-row__rule:last-child { margin-left: 3px; }
  .icon {
    width: 25px; height: 25px;
    background: var(--leaf);
    border-radius: 3px;
    display: flex; align-items: center; justify-content: center;
  }
  .icon svg { width: 15px; height: 15px; }

  .contact {
    position: absolute;
    top: 430px;
    left: 0; right: 0;
    text-align: center;
    font-size: 17px;
    line-height: 22px;
    color: var(--ink);
  }
  .contact__rule {
    position: absolute;
    top: 507px;
    left: 88px;
    width: 196px;
    height: 1px;
    background: var(--rule);
  }
  .address {
    position: absolute;
    top: 518px;
    left: 0; right: 0;
    text-align: center;
    font-size: 17px;
    line-height: 21px;
    color: var(--ink);
  }
</style>
</head>
<body>
  <section class="card card--front" aria-label="Kartenvorderseite">
    <div class="brand">
      <span class="brand__dot"></span>
      <span class="brand__name">Haus solvaKräut</span>
    </div>
  </section>

  <section class="card card--back" aria-label="Kartenrückseite">
    <div class="brand">
      <span class="brand__dot"></span>
      <span class="brand__name">Haus solvaKräut</span>
    </div>

    <div class="person">
      <p class="person__name">Lukas <span class="surname">Brenner</span></p>
      <p class="person__role">Managing Director</p>
    </div>

    <div class="icon-row">
      <span class="icon-row__rule"></span>
      <span class="icon" aria-label="Telefon">
        <svg viewBox="0 0 16 16" fill="#fff"><path d="M2 6c0-2 2.5-3 6-3s6 1 6 3v1h-3V5.5C10 5 9 5 8 5s-2 0-3 .5V7H2z"/><rect x="3" y="8" width="10" height="5" rx="1"/></svg>
      </span>
      <span class="icon" aria-label="E-Mail">
        <svg viewBox="0 0 16 16" fill="none" stroke="#fff" stroke-width="1.3"><rect x="1.5" y="3.5" width="13" height="9"/><path d="M1.5 3.5 8 9l6.5-5.5M1.5 12.5l5-4.5M14.5 12.5l-5-4.5"/></svg>
      </span>
      <span class="icon" aria-label="Web">
        <svg viewBox="0 0 16 16" fill="none" stroke="#fff" stroke-width="1.3"><circle cx="8" cy="8" r="6.3"/><path d="M1.7 8h12.6M8 1.7c-2.5 3-2.5 9.6 0 12.6M8 1.7c2.5 3 2.5 9.6 0 12.6"/></svg>
      </span>
      <span class="icon-row__rule"></span>
    </div>

    <div class="contact">
      <p>044-987 654 321</p>
      <p>praxis@solvakraut.de</p>
      <p>www.solvakraut-haus.de</p>
    </div>
    <div class="contact__rule"></div>
    <div class="address">
      <p>218, Lindenweg Nord</p>
      <p>80331, Deutschland</p>
    </div>
  </section>
</body>
</html>
```